Business Card Design Project Lend Aid

Simple and clean business card,

Logo and fond added in attachment

Data need to be changable:
Ria Vondeck
Customer Service Specialist

Lend Aid - ria.vondeck@lendaid.be - Mob: +32491532876 - www.lendaid.be

Target Market(s)

Small businesses

Industry/Entity Type

Business

Requirements
Nice to have
• QR-code

```html
<!DOCTYPE html>
<html lang="en">
<head>
<meta charset="utf-8">
<title>Lend Aid – Business Card</title>
<link rel="stylesheet" href="https://fonts.googleapis.com/css2?family=Open+Sans:wght@400;600;700&display=swap">
<style>
  :root {
    --brand-blue: #1ea4dc;
    --brand-green: #8cc43c;
    --text-grey: #454545;
    --card-white: #ffffff;
    --backdrop: #eceef0;
    --decor-tint: #e4f3fa;
  }
  html, body {
    margin: 0;
    width: 1200px;
    height: 676px;
    overflow: hidden;
    background: var(--backdrop);
    font-family: "Open Sans", sans-serif;
  }
  .business-card {
    position: absolute;
    left: 220px;
    top: 92px;
    width: 760px;
    height: 492px;
    background: var(--card-white);
    box-shadow: 0 6px 24px rgba(0,0,0,0.12);
  }
  .decor-mark {
    position: absolute;
    left: 110px;
    top: 52px;
    width: 200px;
    height: 200px;
    border: 26px solid var(--decor-tint);
    border-radius: 22px;
    box-sizing: border-box;
  }
  .brand {
    position: absolute;
    right: 60px;
    top: 92px;
    display: flex;
    align-items: center;
    gap: 12px;
  }
  .brand-square {
    width: 40px;
    height: 40px;
    background: var(--brand-blue);
    border-radius: 4px;
  }
  .brand-name {
    font-size: 46px;
    font-weight: 600;
    color: var(--brand-blue);
    line-height: 1;
    letter-spacing: 0.5px;
  }
  .identity {
    position: absolute;
    right: 60px;
    top: 160px;
    text-align: right;
  }
  .person-name {
    margin: 0;
    font-size: 30px;
    font-weight: 700;
    color: var(--brand-blue);
    line-height: 1.15;
  }
  .person-title {
    margin: 2px 0 0;
    font-size: 21px;
    font-weight: 700;
    color: var(--brand-green);
  }
  .contact-list {
    position: absolute;
    right: 60px;
    top: 262px;
    margin: 0;
    padding: 0;
    list-style: none;
  }
  .contact-item {
    display: flex;
    justify-content: flex-end;
    align-items: center;
    gap: 14px;
    height: 40px;
    font-size: 23px;
    color: var(--text-grey);
  }
  .contact-icon {
    width: 26px;
    height: 26px;
    background: var(--brand-blue);
    border-radius: 2px;
    display: flex;
    align-items: center;
    justify-content: center;
  }
  .contact-icon svg { width: 18px; height: 18px; }
</style>
</head>
<body>
  <main class="business-card">
    <div class="decor-mark" aria-hidden="true"></div>

    <div class="brand">
      <span class="brand-square" aria-hidden="true"></span>
      <span class="brand-name">Lend Aid</span>
    </div>

    <div class="identity">
      <h1 class="person-name">Ria Vondeck</h1>
      <p class="person-title">Customer Service Specialist</p>
    </div>

    <ul class="contact-list">
      <li class="contact-item">
        <span class="contact-text">+32491532876</span>
        <span class="contact-icon" aria-hidden="true">
          <svg viewBox="0 0 18 18"><rect x="5" y="2" width="8" height="14" rx="1.5" fill="none" stroke="#fff" stroke-width="1.6"/><line x1="8" y1="13.5" x2="10" y2="13.5" stroke="#fff" stroke-width="1.6"/></svg>
        </span>
      </li>
      <li class="contact-item">
        <span class="contact-text">www.lendaid.be</span>
        <span class="contact-icon" aria-hidden="true">
          <svg viewBox="0 0 18 18" fill="none" stroke="#fff" stroke-width="1.4"><circle cx="9" cy="9" r="6.5"/><ellipse cx="9" cy="9" rx="3" ry="6.5"/><line x1="2.5" y1="9" x2="15.5" y2="9"/></svg>
        </span>
      </li>
      <li class="contact-item">
        <span class="contact-text">ria.vondeck@lendaid.be</span>
        <span class="contact-icon" aria-hidden="true">
          <svg viewBox="0 0 18 18" fill="none" stroke="#fff" stroke-width="1.5"><rect x="2" y="4" width="14" height="10"/><polyline points="2,4 9,10 16,4"/></svg>
        </span>
      </li>
    </ul>
  </main>
</body>
</html>
```